Harbor Resolve presentation and executive summary

Investor wants our presentation to look more professional

Industry/Entity Type

Tech

Font styles to use
Serif

Requirements
Must have
• different design
Nice to have
• different design
Should not have
• any changes in contest

```html
<!DOCTYPE html>
<html lang="en">
<head>
<meta charset="utf-8">
<title>Harbor Resolve — AI-powered Programmatic Ad Mediation</title>
<link rel="stylesheet" href="https://fonts.googleapis.com/css2?family=Playfair+Display:wght@400;600&family=Source+Serif+4:wght@300;400;600&display=swap">
<style>
  :root {
    --page: #fbf9f6;
    --ink-dark: #26221f;
    --ink-light: #ffffff;
    --ink-soft: #e6ddd3;
    --body-grey: #6f6a65;
    --brand-brown: #766659;
    --accent-brown: #9a7b5f;
    --line: #ddd3c8;
    --hero-top: #3b3734;
    --hero-bottom: #1d1b1a;
  }
  * { margin: 0; padding: 0; box-sizing: border-box; }
  html, body { width: 1200px; height: 2782px; overflow: hidden; background: var(--page); }
  body { font-family: "Source Serif 4", Georgia, serif; font-weight: 300; color: var(--ink-dark); }
  .canvas { position: relative; width: 1200px; height: 2782px; overflow: hidden; }

  /* Brand mark (name only) */
  .brand { position: absolute; display: flex; align-items: center; gap: 12px;
    font-family: "Source Serif 4", Georgia, serif; font-weight: 600; letter-spacing: 0.5px; white-space: nowrap; }
  .brand-square { width: 12px; height: 12px; flex: none; }
  .brand--hero { left: 110px; top: 104px; font-size: 30px; color: var(--ink-light); }
  .brand--hero .brand-square { background: var(--accent-brown); }
  .brand--small { right: 54px; font-size: 22px; color: var(--brand-brown); }
  .brand--small .brand-square { background: var(--brand-brown); width: 10px; height: 10px; }

  /* Hero */
  .hero { position: absolute; left: 0; top: 0; width: 1200px; height: 880px;
    background: linear-gradient(160deg, var(--hero-top) 0%, #2c2927 55%, var(--hero-bottom) 100%); }
  .hero-edge { position: absolute; left: 0; top: 0; width: 18px; height: 880px; background: var(--brand-brown); }
  .hero-kicker { position: absolute; left: 110px; top: 336px; font-size: 22px; font-weight: 400;
    letter-spacing: 3px; text-transform: uppercase; color: var(--ink-soft); }
  .hero-title { position: absolute; left: 110px; top: 386px; width: 940px;
    font-family: "Playfair Display", Georgia, serif; font-weight: 400; font-size: 54px; line-height: 66px; color: var(--ink-light); }
  .hero-rule { position: absolute; left: 110px; top: 548px; width: 122px; height: 3px; background: var(--accent-brown); }

  /* Section headings */
  .section-title { position: absolute; left: 54px; font-family: "Playfair Display", Georgia, serif;
    font-size: 42px; font-weight: 400; color: var(--ink-dark); }
  .section-rule { position: absolute; left: 54px; width: 122px; height: 3px; background: var(--brand-brown); }

  /* What we do */
  .mission-band { position: absolute; left: 0; top: 1110px; width: 1200px; height: 260px; background: var(--brand-brown); }
  .mission-text { position: absolute; left: 54px; top: 1158px; width: 580px;
    font-family: "Playfair Display", Georgia, serif; font-size: 40px; line-height: 54px; color: var(--ink-light); font-weight: 400; }
  .mission-text strong { font-weight: 600; }
  .device-art { position: absolute; left: 700px; top: 1060px; width: 420px; height: 560px; border-radius: 28px;
    background: linear-gradient(160deg, #d9d4ce 0%, #8f97a3 45%, #5f7896 100%);
    box-shadow: 0 18px 40px rgba(38, 34, 31, 0.18); }

  /* Pain points */
  .card { position: absolute; width: 520px; border-top: 1px solid var(--line); padding-top: 24px; }
  .card--a { left: 54px; top: 1860px; }
  .card--b { left: 54px; top: 2220px; }
  .card--c { left: 626px; top: 1860px; }
  .card--d { left: 626px; top: 2220px; }
  .card-art { width: 260px; height: 150px; border-radius: 6px; margin-bottom: 22px; }
  .card-art--map { background: linear-gradient(135deg, #4a4542, #7a5d4c); }
  .card-art--tools { background: linear-gradient(135deg, #c9d3e0, #d97a92); }
  .card-art--laptop { background: linear-gradient(160deg, #e07a42 0%, #9aa4b0 60%, #d9d9d9 100%); }
  .card-art--payout { background: linear-gradient(160deg, #f0a830 0%, #d99520 60%, #6a7380 100%); }
  .card-text { font-size: 20px; line-height: 30px; color: var(--body-grey); font-weight: 300; }
  .card-text strong { color: var(--accent-brown); font-weight: 600; }
</style>
</head>
<body>
<main class="canvas">

  <header class="hero" role="img" aria-label="Team working at computer desks in a dim office">
    <div class="hero-edge"></div>
    <div class="brand brand--hero"><span class="brand-square"></span>Harbor Resolve</div>
    <p class="hero-kicker">AI-powered Programmatic Ad Mediation</p>
    <h1 class="hero-title">Automated solution that dramatically increase mobile ad revenues</h1>
    <div class="hero-rule"></div>
  </header>

  <section class="what-we-do">
    <h2 class="section-title" style="top:958px;">What we do</h2>
    <div class="section-rule" style="top:1026px;"></div>
    <div class="brand brand--small" style="top:976px;"><span class="brand-square"></span>Harbor Resolve</div>
    <div class="mission-band"></div>
    <p class="mission-text">Help mobile app <strong>developers</strong> and <strong>publishers</strong> earn a fair share of mobile ad revenue</p>
    <div class="device-art" role="img" aria-label="Smartphone surrounded by a ring of app and media icons"></div>
  </section>

  <section class="pain-points">
    <h2 class="section-title" style="top:1738px;">Pain points we solve</h2>
    <div class="section-rule" style="top:1806px;"></div>
    <div class="brand brand--small" style="top:1756px;"><span class="brand-square"></span>Harbor Resolve</div>

    <article class="card card--a">
      <div class="card-art card-art--map" role="img" aria-label="World map with people and coin symbols"></div>
      <p class="card-text"><strong>Manual ad revenue optimization</strong> takes a lot of human resources and is time consuming. We automate this process very efficiently.</p>
    </article>

    <article class="card card--c">
      <div class="card-art card-art--laptop" role="img" aria-label="Laptop with dashboard windows"></div>
      <p class="card-text">Manual optimization cannot be real-time (millions of constantly changing critical data points). Our <strong>machine learning programmatic solution</strong> instantly solves this issue.</p>
    </article>

    <article class="card card--b">
      <div class="card-art card-art--tools" role="img" aria-label="Magnifier over an app screen with tool icons"></div>
      <p class="card-text">With all the complexity of the industry, developers spend a lot of their time figuring out ad monetization technology, tactics, implementation, etc. By <strong>taking care of all ad monetization</strong> needs and providing significant revenue increase, Harbor Resolve solution allows Pubs and Devs to focus solely on their product.</p>
    </article>

    <article class="card card--d">
      <div class="card-art card-art--payout" role="img" aria-label="Hand dropping a coin into a monitor showing a dollar sign"></div>
      <p class="card-text">Publishers who have not chosen a mediation partner yet, deal with additional accounting, transparency and compatibility issues. <strong>We solve pricing transparency</strong>, providing better revenue share terms, simple accounting by providing one dashboard and single payment, and compatibility issue is solved by a single SDK we provide. Our payouts are instant vs. industry standard Net 30/60 terms.</p>
    </article>
  </section>

</main>
</body>
</html>
```